Business card for auto dealership

Looking for a clean modern design.
Would like attached logo incorporated

Industry/Entity Type

Car dealership

Contact Information for Business Card

Name, website, phone, cell, fax, email

```html
<!DOCTYPE html>
<html lang="en">
<head>
<meta charset="utf-8">
<title>Harlow Truck &amp; Auto Sales – Business Card</title>
<link rel="stylesheet" href="https://fonts.googleapis.com/css2?family=Great+Vibes&family=Roboto:wght@400;700&display=swap">
<style>
  :root {
    --canvas-bg: #d4d4d4;
    --card-white: #ffffff;
    --card-black: #050505;
    --ink: #111111;
    --ink-soft: #333333;
    --paper: #ffffff;
  }
  * { box-sizing: border-box; margin: 0; padding: 0; }
  html, body { width: 1200px; height: 800px; overflow: hidden; }
  body {
    background: var(--canvas-bg);
    font-family: "Roboto", Arial, sans-serif;
    position: relative;
  }
  .card {
    position: absolute;
    top: 250px;
    width: 540px;
    height: 308px;
    border-radius: 22px;
    overflow: hidden;
  }
  .card--front { left: 40px; background: var(--card-white); }
  .card--back { left: 620px; background: var(--card-black); }

  .front__square {
    position: absolute;
    left: 420px; top: 34px;
    width: 80px; height: 66px;
    background: var(--card-black);
  }
  .front__name {
    position: absolute;
    left: 36px; top: 96px;
    font-family: "Great Vibes", cursive;
    font-size: 34px;
    color: var(--ink);
  }
  .front__band {
    position: absolute;
    left: 0; top: 156px;
    width: 290px; height: 96px;
    background: var(--card-black);
    padding: 14px 0 0 40px;
    display: flex; flex-direction: column; gap: 6px;
  }
  .contact-line {
    display: flex; align-items: center; gap: 7px;
    font-size: 15px; letter-spacing: 0.3px;
    white-space: nowrap;
  }
  .front__band .contact-line { color: var(--paper); }
  .front__web {
    position: absolute;
    left: 178px; top: 256px;
    display: flex; flex-direction: column; gap: 4px;
  }
  .front__web .contact-line { color: var(--ink-soft); font-size: 14px; }
  .icon { width: 17px; height: 17px; flex: none; }

  .brand {
    position: absolute;
    display: flex; align-items: center; gap: 8px;
    font-family: "Roboto", Arial, sans-serif;
    font-weight: 700;
    white-space: nowrap;
  }
  .brand__mark { display: block; flex: none; }
  .brand--front { left: 296px; top: 134px; font-size: 16px; color: var(--ink); }
  .brand--front .brand__mark { width: 11px; height: 11px; background: var(--ink); }
  .brand--back { left: 50%; top: 50%; transform: translate(-50%, -50%); font-size: 30px; color: var(--paper); }
  .brand--back .brand__mark { width: 18px; height: 18px; background: var(--paper); }
</style>
</head>
<body>
  <section class="card card--front" aria-label="Business card front">
    <div class="front__square"></div>
    <p class="front__name">Daniel Hart</p>
    <div class="brand brand--front"><span class="brand__mark"></span>Harlow Truck &amp; Auto Sales</div>

    <div class="front__band">
      <p class="contact-line">
        <svg class="icon" viewBox="0 0 20 20" fill="none" stroke="currentColor" stroke-width="1.4"><circle cx="10" cy="10" r="9"/><path d="M7 5.5l1.6 2.4-1 1.2c.7 1.4 1.8 2.5 3.2 3.2l1.2-1 2.4 1.6-.9 1.6c-3.6-.3-7-3.7-7.3-7.3z" fill="currentColor" stroke="none"/></svg>
        044-555 018 240
      </p>
      <p class="contact-line">
        <svg class="icon" viewBox="0 0 20 20" fill="none" stroke="currentColor" stroke-width="1.4"><circle cx="10" cy="10" r="9"/><rect x="7" y="5" width="6" height="10" rx="1"/></svg>
        +91-555 018 241
      </p>
      <p class="contact-line">
        <svg class="icon" viewBox="0 0 20 20" fill="none" stroke="currentColor" stroke-width="1.4"><circle cx="10" cy="10" r="9"/><rect x="6" y="9" width="8" height="5" fill="currentColor" stroke="none"/><rect x="7.5" y="5.5" width="5" height="3"/></svg>
        044-555 018 242
      </p>
    </div>

    <div class="front__web">
      <p class="contact-line">
        <svg class="icon" viewBox="0 0 20 20" fill="none" stroke="currentColor" stroke-width="1.4"><circle cx="10" cy="10" r="9"/><rect x="5.5" y="7" width="9" height="6.5"/><path d="M5.5 7l4.5 3.5L14.5 7"/></svg>
        info@harlowauto.com
      </p>
      <p class="contact-line">
        <svg class="icon" viewBox="0 0 20 20" fill="none" stroke="currentColor" stroke-width="1.4"><circle cx="10" cy="10" r="9"/><circle cx="10" cy="10" r="5"/><path d="M5 10h10M10 5c-2 2.8-2 7.2 0 10M10 5c2 2.8 2 7.2 0 10"/></svg>
        www.harlowauto.com
      </p>
    </div>
  </section>

  <section class="card card--back" aria-label="Business card back">
    <div class="brand brand--back"><span class="brand__mark"></span>Harlow Truck &amp; Auto Sales</div>
  </section>
</body>
</html>
```